Business Card Design Project 4 Construction Business

I am after a creative, but sleek and simple/ clean business card design. This design will form the basis of future items and might include a logo or simply a creative way to lay out the text of my company name 'kestrel ventures'
I like the simplicity of black and white however I would also be happy to see a splash of colour introduced somehow to give the text some interest and make it stand out.
I would like a double sided card.
I am young (ish!) and professional, offering construction and project management services, what I don't want is the traditional builders type card featuring a cheesy hammer/ saw image etc.
As the company name, kestrel ventures, suggests, we focus on working closely and collaboratively together, in synergy with all stakeholders involved in the projects that we undertake
Construction

```html
<!DOCTYPE html>
<html lang="en">
<head>
<meta charset="utf-8">
<title>Kestrel Ventures – Business Card</title>
<link rel="stylesheet" href="https://fonts.googleapis.com/css2?family=Roboto:wght@400;500;900&display=swap">
<style>
  :root {
    --stage: #e4e6e9;
    --blue-deep: #1d82c9;
    --blue-mid: #3a9ddf;
    --blue-light: #6cc3ef;
    --brand-blue: #2b8fd3;
    --ink: #2a2f36;
    --paper: #ffffff;
  }
  * { box-sizing: border-box; margin: 0; padding: 0; }
  html, body {
    width: 1067px; height: 1200px; overflow: hidden;
    background: var(--stage);
    font-family: "Roboto", Arial, sans-serif;
  }
  .canvas { position: relative; width: 1067px; height: 1200px; }
  .card {
    position: absolute; left: 213px; width: 640px; height: 366px;
    border-radius: 3px; overflow: hidden;
    box-shadow: 0 10px 26px rgba(0,0,0,.22);
  }
  .card--front {
    top: 150px;
    background: radial-gradient(ellipse at 50% 40%, var(--blue-light) 0%, var(--blue-mid) 45%, var(--blue-deep) 100%);
    color: var(--paper);
    text-align: center;
  }
  .front__name {
    position: absolute; left: 0; right: 0; top: 132px;
    font-weight: 900; font-size: 52px; letter-spacing: 1px;
    text-transform: uppercase; line-height: 1;
  }
  .front__web {
    position: absolute; left: 0; right: 0; top: 232px;
    font-size: 15px; letter-spacing: .8px;
  }
  .card--back { top: 684px; background: var(--paper); color: var(--ink); }
  .back__brand {
    position: absolute; left: 44px; top: 44px;
    font-weight: 900; font-size: 36px; text-transform: uppercase;
    color: var(--brand-blue); line-height: 1; letter-spacing: .5px;
  }
  .back__person { position: absolute; left: 44px; top: 118px; }
  .person__name { font-size: 19px; color: var(--brand-blue); }
  .person__role { font-size: 13px; margin-top: 2px; }
  .back__address { position: absolute; left: 44px; top: 170px; font-size: 14px; }
  .back__contacts { position: absolute; left: 44px; top: 198px; list-style: none; font-size: 13.5px; }
  .back__contacts li { display: flex; align-items: center; gap: 8px; height: 20px; }
  .back__contacts svg { width: 13px; height: 13px; fill: var(--brand-blue); }
  .back__stripes { position: absolute; left: 0; bottom: 0; width: 640px; height: 160px; }
</style>
</head>
<body>
<main class="canvas">
  <section class="card card--front" aria-label="Card front">
    <h1 class="front__name">Kestrel Ventures</h1>
    <p class="front__web">www.kestrelventures.com.au</p>
  </section>

  <section class="card card--back" aria-label="Card back">
    <p class="back__brand">Kestrel Ventures</p>
    <div class="back__person">
      <p class="person__name">Liam Porter</p>
      <p class="person__role">Director</p>
    </div>
    <p class="back__address">14 Harlow St Chatswood NSW 2067</p>
    <ul class="back__contacts">
      <li>
        <svg viewBox="0 0 24 24" aria-hidden="true"><path d="M6.6 10.8a15.1 15.1 0 0 0 6.6 6.6l2.2-2.2a1 1 0 0 1 1-.25 11.4 11.4 0 0 0 3.6.6 1 1 0 0 1 1 1V20a1 1 0 0 1-1 1A17 17 0 0 1 3 4a1 1 0 0 1 1-1h3.5a1 1 0 0 1 1 1c0 1.25.2 2.45.57 3.57a1 1 0 0 1-.25 1z"/></svg>
        0400 555 182
      </li>
      <li>
        <svg viewBox="0 0 24 24" aria-hidden="true"><path d="M2 5h20v14H2z M2 5l10 8 10-8" fill="none" stroke="currentColor"/><path d="M2 5h20v1.5L12 14 2 6.5z"/><path d="M2 8l10 7.5L22 8v11H2z"/></svg>
        liam@kestrelventures.com.au
      </li>
      <li>
        <svg viewBox="0 0 24 24" aria-hidden="true"><circle cx="12" cy="12" r="10"/></svg>
        www.kestrelventures.com.au
      </li>
    </ul>
    <svg class="back__stripes" viewBox="0 0 640 160" preserveAspectRatio="none" aria-hidden="true">
      <polygon points="300,160 640,40 640,58 352,160" fill="var(--blue-deep)"/>
      <polygon points="380,160 640,72 640,92 440,160" fill="var(--blue-mid)"/>
      <polygon points="470,160 640,106 640,160" fill="var(--blue-deep)"/>
      <rect x="0" y="146" width="640" height="14" fill="var(--blue-mid)"/>
    </svg>
  </section>
</main>
</body>
</html>
```